Real Estate Agency Facebook Cover Photo

We need a Facebook cover photo created for our Real Estate Business. We also need this cover photo adapted to several other platforms. Please read this google doc for full specifications of the job https://papers.vellomarsh.com/sheet/d/8QwPzLk3RtYvB2nHs7JxVaM5_cEdGoUfNpLkZrWbYq/view?mode=shared

Please also carefully read the Must Haves/Should Not Haves

Please contact me if you have any queries. Looking forward to seeing your designs!

Doran

Industry/Entity Type

Real Estate Agent

Requirements
Must have
• The Taglines 'More Money In Your Pocket' and sub tagline 'With Our Low Flat Fee To Sell Your Home'

It can then also have other elements e.g our logo, contact details and anything else you think will work well.

It must also have great graphic design work which looks custom and very clean/modern
Should not have
• Must not have poor quality stock images or anything tacky regarding money etc

```html
<!DOCTYPE html>
<html lang="en">
<head>
<meta charset="utf-8">
<title>Arden – Facebook Cover</title>
<link rel="stylesheet" href="https://fonts.googleapis.com/css2?family=Oswald:wght@400;600&family=Playfair+Display:wght@900&family=Raleway:wght@500&display=swap">
<style>
  :root {
    --stage: #2f4d7a;
    --white: #ffffff;
    --band-grey: #e6e7e9;
    --hex-grey: #e3e4e6;
    --red: #ec1c24;
    --red-deep: #be1e2d;
    --ink: #1f1f1f;
    --bar: #222222;
  }
  html, body {
    margin: 0;
    width: 1200px;
    height: 1200px;
    overflow: hidden;
    background: var(--stage);
  }
  .stage {
    width: 1200px;
    height: 1200px;
    display: flex;
    align-items: center;
    justify-content: center;
  }
  .cover {
    display: block;
    width: 1100px;
    height: 483px;
  }
  .brand { font-family: "Oswald", sans-serif; font-weight: 600; fill: var(--red); }
  .headline { font-family: "Playfair Display", serif; font-weight: 900; fill: var(--ink); }
  .subline { font-family: "Raleway", sans-serif; font-weight: 500; fill: var(--white); }
  .call { font-family: "Oswald", sans-serif; font-weight: 400; fill: var(--white); }
</style>
</head>
<body>
<main class="stage">
  <svg class="cover" viewBox="0 0 1267 556" xmlns="http://www.w3.org/2000/svg" aria-label="Arden cover: More money in your pocket">
    <defs>
      <linearGradient id="tower-tone" x1="0" y1="0" x2="1" y2="1">
        <stop offset="0" stop-color="#f2f2f2"/>
        <stop offset="0.45" stop-color="#5a5a5a"/>
        <stop offset="1" stop-color="#2a2a2a"/>
      </linearGradient>
    </defs>

    <!-- base panels -->
    <rect class="panel-white" width="1267" height="556" fill="var(--white)"/>
    <rect class="panel-grey-band" y="422" width="1267" height="134" fill="var(--band-grey)"/>

    <!-- red side field -->
    <polygon class="side-red" points="935,0 1267,0 1267,556 880,556" fill="var(--red)"/>
    <polygon class="side-red-deep" points="1161,129 1267,70 1267,370 1161,422" fill="var(--red-deep)"/>

    <!-- call-out triangle -->
    <polygon class="call-triangle" points="426,556 655,422 884,556" fill="var(--red-deep)"/>

    <!-- hexagon frame -->
    <polygon class="hex-frame" points="908,-14 1161,129 1161,422 908,566 655,422 655,129" fill="var(--hex-grey)"/>
    <polygon class="hex-photo" role="img" aria-label="Black and white photo of a tall office tower seen from below"
      points="908,34 1121,155 1121,399 908,520 694,399 694,155" fill="url(#tower-tone)"/>

    <!-- wordmark -->
    <text class="brand" x="71" y="139" font-size="72" textLength="300" lengthAdjust="spacingAndGlyphs">ARDEN</text>

    <!-- taglines -->
    <text class="headline" x="71" y="234" font-size="62" textLength="430" lengthAdjust="spacingAndGlyphs">MORE MONEY</text>
    <text class="headline" x="71" y="292" font-size="62" textLength="523" lengthAdjust="spacingAndGlyphs">IN YOUR POCKET</text>

    <rect class="subline-bar" x="0" y="316" width="596" height="49" fill="var(--bar)"/>
    <text class="subline" x="71" y="349" font-size="24" textLength="499" lengthAdjust="spacingAndGlyphs">WITH OUR LOW FLAT FEE TO SELL YOUR HOME</text>

    <!-- contact -->
    <text class="call" x="646" y="492" font-size="34" text-anchor="middle" textLength="94" lengthAdjust="spacingAndGlyphs">CALL US</text>
    <text class="call" x="646" y="535" font-size="38" text-anchor="middle" textLength="204" lengthAdjust="spacingAndGlyphs">+61 2 5550 1842</text>
  </svg>
</main>
</body>
</html>
```